Redesign Our Presentation on Rational Prescribing

We are looking for a new designer for MVQz, a project that creates educational modules for healthcare providers in the Marlow Crest Territory (more information at hlb.example-care.org/mvqz). We want someone to redesign our powerpoints to look clean and professional, with original graphics that reflect the content on the slides. We also want someone who is creative and could potentially also redesign factsheets, written reports, and promotional postcards.

All the text on the slides must stay the same and it must be in the template (red line at the top, with the red box at the bottom, with the MCT Bureau of Wellness logo). We want a powerpoint that features original graphics, looks professional, looks clean and is easy to read.

Industry/Entity Type

Healthcare

```html
<!DOCTYPE html>
<html lang="en">
<head>
<meta charset="utf-8">
<title>Second Generation vs. First Generation</title>
<link href="https://fonts.googleapis.com/css2?family=Carlito:wght@400;700&family=Arimo:wght@400&display=swap" rel="stylesheet">
<style>
  :root {
    --red: #e3131b;
    --title-grey: #4a4a4a;
    --body-ink: #1f1f1f;
    --cite-red: #e8343a;
    --brand-navy: #1c2b5a;
    --paper: #ffffff;
    --photo-light: #e9d9c4;
    --photo-mid: #c9a27f;
    --photo-dark: #8c6a4f;
  }
  html, body {
    margin: 0;
    padding: 0;
    overflow: hidden;
    background: var(--paper);
  }
  .slide {
    position: relative;
    width: 1200px;
    height: 675px;
    overflow: hidden;
    background: var(--paper);
    font-family: "Carlito", "Calibri", sans-serif;
    color: var(--body-ink);
  }
  .slide-title {
    position: absolute;
    left: 86px;
    top: 58px;
    margin: 0;
    width: 600px;
    font-weight: 400;
    font-size: 41px;
    line-height: 1.13;
    color: var(--title-grey);
  }
  .title-rule {
    position: absolute;
    left: 86px;
    top: 161px;
    width: 1095px;
    height: 3px;
    background: var(--red);
  }
  .brand {
    position: absolute;
    left: 990px;
    top: 52px;
    width: 175px;
    display: flex;
    align-items: center;
    gap: 10px;
  }
  .brand-mark {
    flex: none;
    width: 30px;
    height: 30px;
    background: var(--brand-navy);
  }
  .brand-name {
    font-family: "Carlito", sans-serif;
    font-weight: 700;
    font-size: 18px;
    line-height: 1.1;
    color: var(--brand-navy);
    text-transform: uppercase;
  }
  .points {
    position: absolute;
    left: 74px;
    top: 184px;
    width: 530px;
    margin: 0;
    padding: 0;
    list-style: none;
  }
  .point {
    position: relative;
    padding-left: 45px;
    margin-bottom: 14px;
    font-size: 19.5px;
    line-height: 1.16;
  }
  .point::before {
    content: "";
    position: absolute;
    left: 2px;
    top: 6px;
    width: 9px;
    height: 11px;
    border: 1px solid var(--body-ink);
  }
  .sub-points {
    margin: 12px 0 0;
    padding: 0;
    list-style: none;
  }
  .sub-point {
    position: relative;
    padding-left: 33px;
    margin-bottom: 14px;
    font-family: "Arimo", "Arial", sans-serif;
    font-size: 15.5px;
    line-height: 1.2;
  }
  .sub-point::before {
    content: "–";
    position: absolute;
    left: 2px;
    top: 0;
  }
  .cite {
    color: var(--cite-red);
    font-family: "Arimo", "Arial", sans-serif;
  }
  .photo {
    position: absolute;
    left: 623px;
    top: 185px;
    width: 573px;
    height: 440px;
    background: radial-gradient(ellipse at 45% 45%, var(--photo-light) 0%, var(--photo-mid) 60%, var(--photo-dark) 100%);
    box-shadow: 0 0 8px rgba(0, 0, 0, 0.35);
  }
  .footer-band {
    position: absolute;
    left: 0;
    top: 626px;
    width: 1200px;
    height: 49px;
    background: var(--red);
    color: var(--paper);
  }
  .page-number {
    position: absolute;
    left: 75px;
    top: 13px;
    font-family: "Arimo", "Arial", sans-serif;
    font-size: 18px;
  }
  .site-address {
    position: absolute;
    right: 43px;
    top: 11px;
    font-family: "Arimo", "Arial", sans-serif;
    font-size: 21px;
  }
</style>
</head>
<body>
<main class="slide">
  <h1 class="slide-title">“Second Generation” vs. “First Generation”</h1>
  <div class="title-rule"></div>

  <div class="brand">
    <span class="brand-mark"></span>
    <span class="brand-name">MCT Bureau of Wellness</span>
  </div>

  <ul class="points">
    <li class="point">There is no advantage to so-called “second generation” antipsychotics over “first generation” antipsychotics.</li>
    <li class="point">The term “second generation was developed for marketing purposes.”</li>
    <li class="point">“First generation” antipsychotics are just as effective as so-called “second generation” antipsychotics.
      <ul class="sub-points">
        <li class="sub-point">The Federally-funded CLARION study found that halperidol (Calmadol) was just as effective as so-called “second generation” antipsychotics <span class="cite">(Verano 2007 impacts)</span></li>
        <li class="sub-point">The CLARION study made no difference in the sales of SGAs.</li>
      </ul>
    </li>
    <li class="point">“Second generation” antipsychotics do not have fewer adverse effects. Although sold as less likely to cause tardive dyskinesia, “second generation” antipsychotics are just as likely as “first -generation” antipsychotics to cause tardive dyskenesia and other extrapyramidal symptoms <span class="cite">(Tarrant impacts)</span></li>
  </ul>

  <div class="photo" role="img" aria-label="Photo of a younger person's hand gently resting on an older person's hand"></div>

  <footer class="footer-band">
    <span class="page-number">8</span>
    <span class="site-address">www.hlb.example-care.org</span>
  </footer>
</main>
</body>
</html>
```